Small business that sells dolls used in the investigation of sudden infant deaths needs a website de

We need a modern update to our very simple current website. We are a small business that manufactures and sells featureless dolls used in the training and investigation of sudden infant deaths. With our customer base being primarily government organizations we are looking for design that is to the point and functional while also being engaging.
Updates

Target Market(s)

Our target audience are organizations such as government offices and training organizations looking for information about our product. This makes readability and ease-of-use of the design very important.

Number of Pages Required

5+ page

Font styles to use
Serif

Colors

Designer to choose colors to be used in the design.

Requirements
Must have
• Straightforward website focused towards the product being sold. With secondary focus is being how to contact the business and the care and use of the product. The business logo is orange and blue, these colors do not necessarily need to show up in the website design. Darker and muted/contrasting colors would probably be better.
Nice to have
• It would be nice if the website had a professional feel, that is slightly maternal but is not cutesy. Given the nature of our product, we also would like a site that is very respectful for any case that our product might be used in it.

```html
<!DOCTYPE html>
<html lang="en">
<head>
<meta charset="utf-8">
<title>Gentle Watch Dolls</title>
<link rel="stylesheet" href="https://fonts.googleapis.com/css2?family=Montserrat:wght@300;400;500;600;700;800&family=Open+Sans:wght@400;600;700&display=swap">
<style>
:root{
  --navy:#0d2366;
  --nav-text:#1c2f6b;
  --accent:#e8401c;
  --red:#e3171b;
  --ink:#111111;
  --muted:#8a8a8a;
  --faint:#bcbcbc;
  --band:#f2f2f2;
  --white:#ffffff;
  --black:#000000;
  --bottom:#333333;
  --doll:#f2461f;
  --icon:#7c7c7c;
  --logo:#2a8ee0;
}
*{margin:0;padding:0;box-sizing:border-box}
html,body{width:1200px;height:2715px;overflow:hidden}
body{position:relative;font-family:"Open Sans",Arial,sans-serif;background:var(--white);color:var(--ink)}
.abs{position:absolute}
section,header,footer{position:absolute;left:0;width:1200px}

/* header */
.site-header{top:0;height:93px;background:var(--band)}
.brand{left:165px;top:24px;display:flex;align-items:center;gap:10px}
.brand-dot{width:30px;height:30px;border-radius:50%;background:var(--logo)}
.brand-name{font-family:"Montserrat",sans-serif;font-weight:700;font-size:14px;line-height:15px;color:var(--logo)}
.brand-tag{font-size:6px;color:var(--logo);font-weight:400;font-family:"Montserrat",sans-serif}
.main-nav{left:728px;top:38px;display:flex;gap:30px;font-family:"Montserrat",sans-serif;font-weight:600;font-size:12px;color:var(--nav-text)}

/* hero */
.hero{top:93px;height:379px;background:var(--white)}
.hero-title{left:158px;top:48px;width:440px;font-family:"Montserrat",sans-serif;font-weight:500;font-size:29px;line-height:37px;color:var(--ink)}
.hero-text{left:158px;top:180px;width:420px;font-family:"Montserrat",sans-serif;font-size:12.5px;line-height:20px;color:var(--muted)}
.btn-more{left:158px;top:293px;width:186px;height:38px;border-radius:19px;background:var(--accent);color:var(--white);font-family:"Montserrat",sans-serif;font-weight:500;font-size:12px;display:flex;align-items:center;justify-content:center;gap:10px;box-shadow:0 3px 8px rgba(232,64,28,.3)}
.hero-visual{left:755px;top:62px;width:130px;height:258px;border-radius:50px 50px 20px 20px;background:var(--doll)}

/* services */
.services{top:472px;height:238px;background:var(--band)}
.service{top:38px;width:210px;text-align:center}
.service-icon{width:72px;height:72px;margin:0 auto;border-radius:10px;background:linear-gradient(#8d8d8d,#6d6d6d);opacity:.85}
.service h3{margin-top:26px;font-family:"Montserrat",sans-serif;font-weight:700;font-size:22px;color:var(--navy)}
.service p{margin-top:6px;font-size:11.5px;line-height:19px;color:var(--muted);padding:0 12px}

/* shared section heads */
.rule{height:2px;background:var(--ink)}
.section-head{font-family:"Montserrat",sans-serif;font-weight:800;font-size:31px;letter-spacing:9px;color:var(--ink)}

/* about */
.about{top:710px;height:345px;background:var(--white)}
.about-copy{left:417px;top:77px;width:573px;font-size:11.5px;line-height:19px;color:var(--faint)}
.about-copy strong{color:var(--red);font-weight:700}
.about-quote{display:block;text-align:center;color:var(--ink);font-weight:700;margin:18px 0}

/* stats */
.stats{top:1055px;height:233px;background:var(--band)}
.stat{top:72px;width:260px;text-align:center}
.stat-num{font-family:"Montserrat",sans-serif;font-weight:300;font-size:50px;line-height:56px;color:var(--navy)}
.stat-label{margin-top:4px;font-family:"Montserrat",sans-serif;font-size:13.5px;color:var(--muted)}

/* contact */
.contact{top:1288px;height:455px;background:var(--white)}
.contact-info{left:527px;top:147px;font-size:11.5px;line-height:17px;color:var(--ink)}
.contact-info b{font-weight:700}
.contact-hours{color:var(--faint);margin-top:28px}
.social{display:flex;gap:28px;margin-top:30px}
.social span{width:12px;height:12px;border-radius:50%;background:var(--ink)}
.field{left:768px;width:336px;height:32px;border:1px solid #d8d8d8;background:var(--white);font-size:11px;color:#777;padding:7px 10px}
.btn-send{left:768px;top:340px;width:336px;height:36px;background:var(--black);color:var(--white);font-family:"Montserrat",sans-serif;font-weight:700;font-size:11px;display:flex;align-items:center;justify-content:center}

/* faq */
.faq{top:1743px;height:732px;background:var(--band)}
.faq-item{width:385px}
.faq-q{display:flex;justify-content:space-between;align-items:center;font-family:"Montserrat",sans-serif;font-weight:700;font-size:12.5px;color:var(--red)}
.faq-q svg{flex:none}
.faq-a{margin-top:14px;font-size:11.5px;line-height:19px;color:var(--faint);width:385px}
.faq-card{left:655px;top:315px;width:447px;height:160px;box-shadow:0 6px 6px -4px rgba(0,0,0,.12)}

/* order footer */
.order{top:2475px;height:200px;background:var(--black)}
.order-head{left:60px;top:66px;font-family:"Montserrat",sans-serif;font-weight:700;font-size:32px;letter-spacing:7px;color:var(--white)}
.btn-pill{left:507px;width:165px;height:34px;border-radius:17px;font-family:"Montserrat",sans-serif;font-weight:700;font-size:10.5px;display:flex;align-items:center;justify-content:center}
.btn-buy{top:58px;background:var(--navy);color:var(--white)}
.btn-tell{top:106px;background:var(--white);color:var(--ink)}
.foot-col{top:26px;color:var(--white);font-size:11px}
.foot-col h4{font-family:"Montserrat",sans-serif;font-weight:700;font-size:13px;margin-bottom:10px}
.foot-col li{list-style:none;line-height:20px;color:#ddd}
.foot-col li::before{content:"›";margin-right:9px;color:#aaa}
.bottom-bar{top:2675px;height:40px;background:var(--bottom)}
.copyright{left:150px;top:13px;font-size:10.5px;color:#999}
</style>
</head>
<body>

<header class="site-header">
  <div class="abs brand">
    <span class="brand-dot"></span>
    <div>
      <div class="brand-name">Gentle Watch<br>Dolls</div>
      <div class="brand-tag">Investigation training dolls</div>
    </div>
  </div>
  <nav class="abs main-nav"><span>About</span><span>FAQ</span><span>Get In Touch</span><span>Place an Order</span></nav>
</header>

<section class="hero">
  <h1 class="abs hero-title">The Only Way To Thoroughly Investigate Infant Death Compassionately</h1>
  <p class="abs hero-text">I am text block. Click edit button to change this text. Lorem ipsum dolor sit amet, consectetur adipiscing elit. Ut elit tellus, luctus nec ullamcorper mattis, pulvinar dapibus leo.</p>
  <div class="abs btn-more">More Information
    <svg width="12" height="8" viewBox="0 0 12 8"><path d="M0 4h10M7 1l3 3-3 3" stroke="#fff" stroke-width="1.6" fill="none"/></svg>
  </div>
  <div class="abs hero-visual" role="img" aria-label="Orange featureless investigation doll standing upright"></div>
</section>

<section class="services">
  <div class="abs service" style="left:157px">
    <div class="service-icon" role="img" aria-label="Magnifying glass with badge icon"></div>
    <h3>Investigators</h3><p>Lorem Ipsum is simply dummy text of the printing</p>
  </div>
  <div class="abs service" style="left:382px">
    <div class="service-icon" role="img" aria-label="Trainer at a presentation board icon"></div>
    <h3>Training</h3><p>Lorem Ipsum is simply dummy text of the printing</p>
  </div>
  <div class="abs service" style="left:607px">
    <div class="service-icon" role="img" aria-label="Police officer icon"></div>
    <h3>Law Enforcement</h3><p>Lorem Ipsum is simply dummy text of the printing</p>
  </div>
  <div class="abs service" style="left:832px">
    <div class="service-icon" role="img" aria-label="Stack of books icon"></div>
    <h3>Resources</h3><p>Lorem Ipsum is simply dummy text of the printing</p>
  </div>
</section>

<section class="about">
  <div class="abs rule" style="left:96px;top:90px;width:254px"></div>
  <h2 class="abs section-head" style="left:96px;top:115px">ABOUT</h2>
  <div class="abs about-copy">
    <p><strong>Our partnership</strong> started with a quilt for a newborn baby that was found in a plastic bag in our community. Her quilt, along with several others, was taken to our county coroner, who told others of our mission to</p>
    <span class="about-quote">“Use the talents the Lord gave us to help others.”</span>
    <p>The Safe Cradle Foundation contacted us about making dolls for investigators. With their help we have designed a doll that we have made available to the sudden, unexplained infant death (SUID) investigation community.</p>
  </div>
</section>

<section class="stats">
  <div class="abs stat" style="left:190px"><div class="stat-num">3,500+</div><div class="stat-label">SUID Every Year</div></div>
  <div class="abs stat" style="left:470px"><div class="stat-num">34%</div><div class="stat-label">Deaths from Unknow Cause</div></div>
  <div class="abs stat" style="left:748px"><div class="stat-num">59%</div><div class="stat-label">Decrease in SUID since 1990</div></div>
</section>

<section class="contact">
  <div class="abs rule" style="left:96px;top:118px;width:384px"></div>
  <h2 class="abs section-head" style="left:96px;top:143px">GET IN TOUCH</h2>
  <div class="abs contact-info">
    <b>Phone: (555) 014-2290</b><br><b>Email: hello@gentlewatchdolls.com</b>
    <p style="margin-top:35px">Gentle Watch Dolls<br>48 Cedar Hollow Rd<br>Fairbrook, WA 98000</p>
    <p class="contact-hours">Monday - Friday:<br>8:00am - 5:00pm Pacific Time</p>
    <div class="social"><span></span><span></span><span></span></div>
  </div>
  <div class="abs field" style="top:146px">Name</div>
  <div class="abs field" style="top:195px">Email</div>
  <div class="abs field" style="top:244px;height:78px">Message</div>
  <div class="abs btn-send">SEND MESSAGE</div>
</section>

<section class="faq">
  <div class="abs rule" style="left:96px;top:92px;width:121px"></div>
  <h2 class="abs section-head" style="left:96px;top:117px">FAQ</h2>
  <div class="abs faq-card"></div>

  <div class="abs faq-item" style="left:226px;top:127px">
    <div class="faq-q">WHAT COLOR ARE THE DOLLS?<svg width="12" height="12" viewBox="0 0 12 12"><circle cx="6" cy="6" r="5" fill="none" stroke="#e3171b" stroke-width="1.4"/><path d="M3.5 5l2.5 2.5L8.5 5" fill="none" stroke="#e3171b" stroke-width="1.4"/></svg></div>
    <p class="faq-a">I am item content. Click edit button to change this text. Lorem ipsum dolor sit amet, consectetur adipiscing elit. Ut elit tellus, luctus nec ullamcorper mattis, pulvinar dapibus leo.</p>
  </div>
  <div class="abs faq-item" style="left:687px;top:127px">
    <div class="faq-q">CAN THEY BE CLEANED?<svg width="12" height="12" viewBox="0 0 12 12"><circle cx="6" cy="6" r="5" fill="none" stroke="#e3171b" stroke-width="1.4"/><path d="M3.5 5l2.5 2.5L8.5 5" fill="none" stroke="#e3171b" stroke-width="1.4"/></svg></div>
    <p class="faq-a">I am item content. Click edit button to change this text. Lorem ipsum dolor sit amet, consectetur adipiscing elit. Ut elit tellus, luctus nec ullamcorper mattis, pulvinar dapibus leo.</p>
  </div>
  <div class="abs faq-item" style="left:226px;top:324px">
    <div class="faq-q">HOW MUCH DO THE DOLLS WEIGH?<svg width="12" height="12" viewBox="0 0 12 12"><circle cx="6" cy="6" r="5" fill="none" stroke="#e3171b" stroke-width="1.4"/><path d="M3.5 5l2.5 2.5L8.5 5" fill="none" stroke="#e3171b" stroke-width="1.4"/></svg></div>
    <p class="faq-a">I am item content. Click edit button to change this text. Lorem ipsum dolor sit amet, consectetur adipiscing elit. Ut elit tellus, luctus nec ullamcorper mattis, pulvinar dapibus leo.</p>
  </div>
  <div class="abs faq-item" style="left:687px;top:324px">
    <div class="faq-q">WHATS THE BEST WAY TO HANDLE THE DOLLS?<svg width="12" height="12" viewBox="0 0 12 12"><circle cx="6" cy="6" r="5" fill="none" stroke="#e3171b" stroke-width="1.4"/><path d="M3.5 5l2.5 2.5L8.5 5" fill="none" stroke="#e3171b" stroke-width="1.4"/></svg></div>
    <p class="faq-a">I am item content. Click edit button to change this text. Lorem ipsum dolor sit amet, consectetur adipiscing elit. Ut elit tellus, luctus nec ullamcorper mattis, pulvinar dapibus leo.</p>
  </div>
  <div class="abs faq-item" style="left:226px;top:521px">
    <div class="faq-q">ARE THEY WATER RESISTANT?<svg width="12" height="12" viewBox="0 0 12 12"><circle cx="6" cy="6" r="5" fill="none" stroke="#e3171b" stroke-width="1.4"/><path d="M3.5 5l2.5 2.5L8.5 5" fill="none" stroke="#e3171b" stroke-width="1.4"/></svg></div>
    <p class="faq-a">I am item content. Click edit button to change this text. Lorem ipsum dolor sit amet, consectetur adipiscing elit. Ut elit tellus, luctus nec ullamcorper mattis, pulvinar dapibus leo.</p>
  </div>
  <div class="abs faq-item" style="left:687px;top:521px">
    <div class="faq-q">ARE CUSTOM DOLLS AVAILABLE<svg width="12" height="12" viewBox="0 0 12 12"><circle cx="6" cy="6" r="5" fill="none" stroke="#e3171b" stroke-width="1.4"/><path d="M3.5 5l2.5 2.5L8.5 5" fill="none" stroke="#e3171b" stroke-width="1.4"/></svg></div>
    <p class="faq-a">I am item content. Click edit button to change this text. Lorem ipsum dolor sit amet, consectetur adipiscing elit. Ut elit tellus, luctus nec ullamcorper mattis, pulvinar dapibus leo.</p>
  </div>
</section>

<footer class="order">
  <div class="abs rule" style="left:60px;top:42px;width:437px;background:var(--white)"></div>
  <h2 class="abs order-head">PLACE AN ORDER</h2>
  <div class="abs btn-pill btn-buy">BUY NOW</div>
  <div class="abs btn-pill btn-tell">TELL ME MORE</div>
  <div class="abs foot-col" style="left:838px"><h4>Dolls</h4><ul><li>Pricing</li><li>Education</li><li>Refer a friend</li></ul></div>
  <div class="abs foot-col" style="left:983px"><h4>Get Started</h4><ul><li>Tutorial</li><li>Resources</li><li>Guides</li><li>Examples</li></ul></div>
</footer>
<div class="abs bottom-bar" style="left:0;width:1200px"><span class="abs copyright">© All rights reserved</span></div>

</body>
</html>
```